Halvorn Homes-Real Estate of the Future

Halvorn Homes is a Residential Real Estate company which specializes in buying and selling homes. We pride ourselves on service, expertise, and building relationships. I would like to do a Billboard Ad for a The Size is 14 feet (Height) x 48 feet (width) displaying our current motto for "Real Estate of the Future" We have launched new programs and working with leaders in our industy Brimlot and other tech companies and changing the way Real Estate is done in Las Vegas, NV. Its exciting and NEW so we want to get the word out. Color Scheme Red, White, Grey and maybe black. Logo is uploaded and so is a picture head shot. I would like to see options with my headshot and with out.

```html
<!DOCTYPE html>
<html lang="en">
<head>
<meta charset="utf-8">
<title>Halvorn Homes – Billboard Options</title>
<link rel="stylesheet" href="https://fonts.googleapis.com/css2?family=Marcellus&display=swap">
<style>
  :root {
    --red: #c8102e;
    --red-bright: #d70a24;
    --red-deep: #6a0914;
    --red-dark: #4e0610;
    --grey-text: #3b3e43;
    --rule: #4a4a4a;
    --white: #ffffff;
    --photo-leaf: #4f6b3a;
    --photo-shade: #2b3a22;
    --photo-warm: #9a7a52;
  }
  html, body {
    margin: 0;
    padding: 0;
    width: 1200px;
    height: 1105px;
    overflow: hidden;
    background: var(--white);
  }
  .board-sheet {
    position: relative;
    width: 1200px;
    height: 1105px;
  }
  .billboard {
    position: absolute;
    left: 0;
    width: 1200px;
    height: 350px;
    display: block;
  }
  .billboard--with-phone-band { top: 170px; }
  .billboard--phone-above-band { top: 570px; }
  .brand-name {
    font-family: "Marcellus", serif;
    font-size: 60px;
    letter-spacing: 3px;
    fill: var(--red);
  }
  .phone {
    font-family: "Marcellus", serif;
    font-size: 50px;
    letter-spacing: 5px;
  }
  .phone--on-band { fill: var(--white); }
  .phone--on-white { fill: var(--grey-text); }
  .tagline {
    font-family: "Marcellus", serif;
    font-size: 27px;
    letter-spacing: 1.5px;
    fill: var(--white);
  }
  .top-rule { stroke: var(--rule); stroke-width: 1; }
</style>
</head>
<body>
<main class="board-sheet">

  <svg class="billboard billboard--with-phone-band" viewBox="0 0 1200 350" xmlns="http://www.w3.org/2000/svg">
    <defs>
      <linearGradient id="headshot-tones-a" x1="0" y1="0" x2="1" y2="1">
        <stop offset="0" stop-color="var(--photo-warm)"/>
        <stop offset="0.45" stop-color="var(--photo-leaf)"/>
        <stop offset="1" stop-color="var(--photo-shade)"/>
      </linearGradient>
      <linearGradient id="band-red-a" x1="0" y1="0" x2="1" y2="0">
        <stop offset="0" stop-color="var(--red-deep)"/>
        <stop offset="0.3" stop-color="var(--red-bright)"/>
        <stop offset="0.65" stop-color="#8e0a1c"/>
        <stop offset="1" stop-color="var(--red-dark)"/>
      </linearGradient>
    </defs>
    <path role="img" aria-label="Headshot of the agent in a navy blazer, garden backdrop"
          d="M0,0 H445 C498,70 500,230 360,335 L0,335 Z" fill="url(#headshot-tones-a)"/>
    <line class="top-rule" x1="0" y1="0.5" x2="499" y2="0.5"/>
    <text class="brand-name" x="844" y="118" text-anchor="middle">HALVORN HOMES</text>
    <path d="M0,250 C80,300 170,330 260,326 C380,318 470,245 590,222 C700,202 880,196 1000,206 C1100,216 1160,252 1200,278 V350 H0 Z"
          fill="url(#band-red-a)"/>
    <path d="M432,350 C640,300 900,285 1200,302 V350 Z" fill="var(--red-dark)" opacity="0.55"/>
    <text class="phone phone--on-band" x="826" y="280" text-anchor="middle">702-555-0148</text>
    <text class="tagline" x="832" y="331" text-anchor="middle">REAL ESTATE OF THE FUTURE</text>
  </svg>

  <svg class="billboard billboard--phone-above-band" viewBox="0 0 1200 350" xmlns="http://www.w3.org/2000/svg">
    <defs>
      <linearGradient id="headshot-tones-b" x1="0" y1="0" x2="1" y2="1">
        <stop offset="0" stop-color="var(--photo-warm)"/>
        <stop offset="0.45" stop-color="var(--photo-leaf)"/>
        <stop offset="1" stop-color="var(--photo-shade)"/>
      </linearGradient>
      <linearGradient id="band-red-b" x1="0" y1="0" x2="1" y2="0">
        <stop offset="0" stop-color="var(--red-deep)"/>
        <stop offset="0.3" stop-color="#9a0a1e"/>
        <stop offset="0.62" stop-color="var(--red-bright)"/>
        <stop offset="1" stop-color="var(--red-dark)"/>
      </linearGradient>
    </defs>
    <path role="img" aria-label="Headshot of the agent in a navy blazer, garden backdrop"
          d="M0,0 H445 C498,70 500,230 360,335 L0,335 Z" fill="url(#headshot-tones-b)"/>
    <line class="top-rule" x1="0" y1="0.5" x2="499" y2="0.5"/>
    <text class="brand-name" x="844" y="118" text-anchor="middle">HALVORN HOMES</text>
    <text class="phone phone--on-white" x="862" y="237" text-anchor="middle">702-555-0148</text>
    <path d="M0,250 C80,300 170,330 260,326 C470,318 620,258 820,254 C980,251 1120,264 1200,278 V350 H0 Z"
          fill="url(#band-red-b)"/>
    <path d="M432,350 C640,312 900,300 1200,308 V350 Z" fill="var(--red-dark)" opacity="0.55"/>
    <text class="tagline" x="852" y="341" text-anchor="middle">REAL ESTATE OF THE FUTURE</text>
  </svg>

</main>
</body>
</html>
```